ACV & Honey RTD

I need a label to go on our 250 ml bottle for our new ready-to-drink Apple Cider Vinegar and Honey drink.

Need a name that doesn't put the buyer off like "vinegar" does but still gives and idea of something a bit different "Elixir" with a bit of a bite' but very good for you

this is for export to Asia and is focused on the health, functional drink market

The logo is attached to this brief.

Would Honey & ACV R2D Work better for name

It looks like I can use the name "Plumvane Draught" now so I hope this clarifies the name issue, Sorry for this late change

Industry/Entity Type

Health

```html
<!DOCTYPE html>
<html lang="en">
<head>
<meta charset="utf-8">
<title>Plumvane Draught — 250 ml label</title>
<link rel="stylesheet" href="https://fonts.googleapis.com/css2?family=Noto+Serif:wght@700&family=Open+Sans:ital,wght@0,600;0,700;1,600;1,700&display=swap">
<style>
  :root {
    --canvas: #ffffff;
    --label-brown: #4a3f39;
    --label-stripe: #564a43;
    --accent-orange: #f2a431;
    --accent-green: #8dc63f;
    --ribbon-red: #c4262e;
    --ribbon-fold: #7e161b;
    --ink-light: #ffffff;
    --badge-grey: #cfc8c2;
    --art-warm: #d9532f;
    --art-soft: #b8402c;
  }
  * { margin: 0; padding: 0; box-sizing: border-box; }
  html, body {
    width: 1200px;
    height: 1000px;
    overflow: hidden;
    background: var(--canvas);
  }
  .canvas {
    position: relative;
    width: 1200px;
    height: 1000px;
  }
  .bottle-label {
    position: absolute;
    left: 300px;
    top: 74px;
    width: 600px;
    height: 852px;
    background: repeating-linear-gradient(
      90deg,
      var(--label-brown) 0 26px,
      var(--label-stripe) 26px 52px
    );
    box-shadow: 0 6px 24px rgba(0,0,0,0.18);
  }
  .bottle-label svg { display: block; }
  .brand-name {
    font-family: "Open Sans", sans-serif;
    font-weight: 700;
    font-size: 24px;
    fill: var(--ink-light);
  }
  .brand-sub {
    font-family: "Noto Serif", serif;
    font-weight: 700;
    font-size: 17px;
    letter-spacing: 1px;
    fill: var(--ink-light);
  }
  .tagline-green {
    font-family: "Open Sans", sans-serif;
    font-style: italic;
    font-weight: 600;
    font-size: 26px;
    fill: var(--accent-green);
  }
  .tagline-green .emph { font-size: 31px; }
  .product-name {
    font-family: "Noto Serif", serif;
    font-weight: 700;
    font-size: 46px;
    fill: var(--ink-light);
  }
  .origin-line {
    font-family: "Open Sans", sans-serif;
    font-style: italic;
    font-weight: 700;
    font-size: 27px;
    fill: var(--accent-orange);
  }
  .volume {
    font-family: "Open Sans", sans-serif;
    font-style: italic;
    font-weight: 600;
    font-size: 34px;
    fill: var(--ink-light);
  }
</style>
</head>
<body>
<main class="canvas">
  <section class="bottle-label" aria-label="Plumvane Draught bottle label">
    <svg width="600" height="852" viewBox="0 0 600 852" xmlns="http://www.w3.org/2000/svg">
      <defs>
        <linearGradient id="artTone" x1="0" y1="0" x2="1" y2="1">
          <stop offset="0%" stop-color="var(--accent-orange)"/>
          <stop offset="55%" stop-color="var(--art-warm)"/>
          <stop offset="100%" stop-color="var(--art-soft)"/>
        </linearGradient>
      </defs>

      <g class="brand">
        <circle cx="300" cy="92" r="14" fill="var(--ink-light)"/>
        <text class="brand-name" x="300" y="136" text-anchor="middle">Rimuvale</text>
        <text class="brand-sub" x="300" y="162" text-anchor="middle">ORGANIC</text>
      </g>

      <path d="M0 244 Q300 160 600 244" fill="none" stroke="var(--accent-orange)" stroke-width="6"/>
      <text class="tagline-green" x="300" y="240" text-anchor="middle">naturally fermented</text>

      <rect class="fruit-art" x="200" y="262" width="200" height="146" rx="10"
            fill="url(#artTone)" opacity="0.9"
            role="img" aria-label="Illustration of red fruit with leaves on an orange sunburst"/>

      <g class="ribbon">
        <polygon points="0,458 96,458 96,566 0,566 34,512" fill="var(--ribbon-red)"/>
        <polygon points="600,458 504,458 504,566 600,566 566,512" fill="var(--ribbon-red)"/>
        <polygon points="58,532 96,532 96,566" fill="var(--ribbon-fold)"/>
        <polygon points="542,532 504,532 504,566" fill="var(--ribbon-fold)"/>
        <rect x="58" y="412" width="484" height="120" fill="var(--ribbon-red)"/>
        <text class="product-name" x="300" y="488" text-anchor="middle">Plumvane Draught</text>
      </g>

      <text class="origin-line" x="300" y="572" text-anchor="middle">Made with passion</text>
      <text class="origin-line" x="300" y="606" text-anchor="middle">in New Zeland</text>

      <path d="M0 612 Q300 760 600 612" fill="none" stroke="var(--accent-orange)" stroke-width="6"/>
      <text class="tagline-green" x="300" y="652" text-anchor="middle">natured in <tspan class="emph">Oak barrels</tspan></text>

      <circle class="cert-badge" cx="113" cy="752" r="40" fill="none" stroke="var(--badge-grey)" stroke-width="4"/>
      <text class="volume" x="300" y="768" text-anchor="middle">250 ml</text>
      <circle class="cert-badge" cx="478" cy="748" r="40" fill="none" stroke="var(--badge-grey)" stroke-width="4"/>
    </svg>
  </section>
</main>
</body>
</html>
```